Marlowe Holdings LLC - Business Cards

Need the following information on the cards:

Name: Dean R Vossler
Title: Chief Executive Manager

Business address:
412 N Ridgeview Lane #118
Elmford Park, NV 60412

Phone: (410) 555-0148 - Business
KPV FFL license number: 5-21-xxx-xx-xx-04519
Email: dean.vossler@marloweholdingsffl.com

Target Market(s)

Firearm owners

Industry/Entity Type

Firearms industry,

Contact Information for Business Card

Contact number, name and title, web page address, email, business address and kpv license number,

Requirements
Must have
• Name, title, business address, phone numbers, KPV license numbers, web page address and email address.
Nice to have
• Cellphone number,

```html
<!DOCTYPE html>
<html lang="en">
<head>
<meta charset="utf-8">
<title>Marlowe Holdings LLC – Business Cards</title>
<link href="https://fonts.googleapis.com/css2?family=Crimson+Text:wght@400;600&display=swap" rel="stylesheet">
<style>
  :root {
    --backdrop: #5a5a5c;
    --card-dark: #262628;
    --card-light: #3c3c3f;
    --brand-red: #c8191f;
    --text-light: #f1f1f1;
  }
  * { margin: 0; padding: 0; box-sizing: border-box; }
  html, body { width: 1200px; height: 900px; overflow: hidden; }
  body {
    background: var(--backdrop);
    font-family: "Crimson Text", Georgia, serif;
    position: relative;
  }
  .card {
    position: absolute;
    left: 285px;
    width: 630px;
    height: 360px;
    overflow: hidden;
    background: linear-gradient(160deg, var(--card-light) 0%, var(--card-dark) 70%);
    box-shadow: 0 10px 24px rgba(0,0,0,.35);
  }
  .card--front { top: 60px; }
  .card--back { top: 480px; }
  .card__band { position: absolute; inset: 0; width: 100%; height: 100%; }

  .brand {
    position: absolute;
    top: 40px;
    right: 34px;
    display: flex;
    align-items: center;
    gap: 12px;
  }
  .brand__circle {
    width: 34px; height: 34px;
    border: 2px solid var(--text-light);
    border-radius: 50%;
  }
  .brand__name {
    color: var(--brand-red);
    font-size: 26px;
    font-weight: 600;
    line-height: 1;
  }
  .card--back .brand { top: 34px; }
  .card--back .brand__name { font-size: 22px; }

  .website-front {
    position: absolute;
    top: 44px;
    left: 34px;
    color: var(--text-light);
    font-size: 15px;
    letter-spacing: .5px;
  }
  .website-front span { color: var(--brand-red); }

  .dog-art {
    position: absolute;
    background: linear-gradient(180deg, rgba(200,25,31,.55), rgba(200,25,31,.2));
    border-radius: 40% 40% 8% 8%;
  }
  .card--front .dog-art { left: 150px; top: 175px; width: 110px; height: 140px; }
  .card--back .dog-art { left: 440px; top: 150px; width: 170px; height: 90px; }

  .person {
    position: absolute;
    left: 36px;
    top: 40px;
  }
  .person__name {
    color: var(--brand-red);
    font-size: 26px;
    font-weight: 600;
    line-height: 1.1;
  }
  .person__title {
    color: var(--text-light);
    font-size: 19px;
  }
  .contacts {
    position: absolute;
    left: 36px;
    top: 128px;
    list-style: none;
    color: var(--text-light);
    font-size: 17px;
  }
  .contacts li {
    display: flex;
    align-items: center;
    gap: 10px;
    height: 27px;
  }
  .contacts svg { width: 15px; height: 15px; fill: var(--brand-red); flex: none; }
  .contacts .divider {
    height: 1px;
    width: 520px;
    background: var(--brand-red);
    margin: 6px 0;
  }
  .license {
    position: absolute;
    left: 36px;
    bottom: 20px;
    color: var(--text-light);
    font-size: 19px;
    letter-spacing: .4px;
  }
</style>
</head>
<body>

  <section class="card card--front">
    <svg class="card__band" viewBox="0 0 630 360" preserveAspectRatio="none" aria-hidden="true">
      <path d="M0 322 L200 308 C300 300 420 262 630 212 L630 360 L0 360 Z" fill="var(--brand-red)"/>
    </svg>
    <p class="website-front">www.<span>marloweholdingsffl</span>.com</p>
    <div class="brand">
      <span class="brand__circle"></span>
      <span class="brand__name">Marlowe Holdings LLC</span>
    </div>
    <div class="dog-art" role="img" aria-label="Red line illustration of a standing shepherd dog"></div>
  </section>

  <section class="card card--back">
    <svg class="card__band" viewBox="0 0 630 360" preserveAspectRatio="none" aria-hidden="true">
      <path d="M0 312 L380 286 C470 280 540 250 630 230 L630 360 L0 360 Z" fill="var(--brand-red)"/>
    </svg>
    <div class="brand">
      <span class="brand__circle"></span>
      <span class="brand__name">Marlowe Holdings LLC</span>
    </div>
    <div class="dog-art" role="img" aria-label="Red line illustration of a walking shepherd dog"></div>

    <div class="person">
      <h1 class="person__name">Dean R Vossler</h1>
      <p class="person__title">Chief Executive Manager</p>
    </div>

    <ul class="contacts">
      <li>
        <svg viewBox="0 0 16 16"><path d="M4 1h8a1 1 0 0 1 1 1v12a1 1 0 0 1-1 1H4a1 1 0 0 1-1-1V2a1 1 0 0 1 1-1zm1 2v9h6V3zm3 10a.8.8 0 1 0 0 .1z"/></svg>
        (410) 555-0148
      </li>
      <li>
        <svg viewBox="0 0 16 16"><path d="M8 1a7 7 0 1 0 0 14A7 7 0 0 0 8 1zm0 1.5c.8 0 1.7 1.6 2 4H6c.3-2.4 1.2-4 2-4zM6 8h4c-.1 2.9-1.1 5.5-2 5.5S6.1 10.9 6 8zM2.6 8h2c0 1.9.4 3.6 1 4.7A5.5 5.5 0 0 1 2.6 8zm8.8 0h2a5.5 5.5 0 0 1-3 4.7c.6-1.1 1-2.8 1-4.7z"/></svg>
        www.marloweholdingsffl.com
      </li>
      <li>
        <svg viewBox="0 0 16 16"><path d="M1 4h14v9H1zm1.5 1.2v.4L8 9l5.5-3.4v-.4z"/></svg>
        dean.vossler@marloweholdingsffl.com
      </li>
      <li class="divider" aria-hidden="true"></li>
      <li>
        <svg viewBox="0 0 16 16"><path d="M8 1a5 5 0 0 0-5 5c0 3.6 5 9 5 9s5-5.4 5-9a5 5 0 0 0-5-5zm0 7a2 2 0 1 1 0-4 2 2 0 0 1 0 4z"/></svg>
        412 N Ridgeview Lane #118, Elmford Park, NV 60412
      </li>
    </ul>

    <p class="license">KPV FFL License Number: 5-21-xxx-xx-xx-04519</p>
  </section>

</body>
</html>
```